Business Card for Holistic Health Business
Bright Ferns Natural Wellness & Live Cell Review
Use same font as used in my logo
Not sure, I am open to different fonts.
Simple
Marla Dunwoody
DynBC, CH, BA
Larkvale Acupuncture Clinic
2736-18 Avenue, Suite 200
Larkvale, AB T8K 2P6
brightferns@mailnest.ca
www.brightfernsnaturalwellness.com
Logo for Bright Ferns business card.

```html
<!DOCTYPE html>
<html lang="en">
<head>
<meta charset="utf-8">
<title>Bright Ferns – Business Card</title>
<link rel="stylesheet" href="https://fonts.googleapis.com/css2?family=Open+Sans:ital,wght@0,400;0,600;1,400;1,600&display=swap">
<style>
  :root {
    --stage: #e6e7ea;
    --paper: #ffffff;
    --blue: #3f87d4;
    --blue-light: #6aa7e6;
    --blue-dark: #2f6fb8;
    --ink: #1c1c1c;
    --grey: #6b6f75;
    --black: #111111;
  }
  * { margin: 0; padding: 0; box-sizing: border-box; }
  html, body { width: 1200px; height: 895px; overflow: hidden; }
  body {
    background: var(--stage);
    font-family: "Open Sans", Arial, sans-serif;
    position: relative;
  }
  .card {
    position: absolute;
    top: 292px;
    width: 540px;
    height: 310px;
    overflow: hidden;
    box-shadow: 0 6px 18px rgba(0,0,0,0.18);
  }
  .card-front { left: 40px; background: var(--paper); }
  .card-back {
    left: 620px;
    background: linear-gradient(160deg, var(--blue-light) 0%, var(--blue) 55%, var(--blue-dark) 100%);
  }
  .front-swoosh { position: absolute; left: 0; top: 0; width: 540px; height: 310px; }

  .brand { position: absolute; left: 34px; top: 34px; }
  .brand-name {
    display: flex; align-items: center; gap: 10px;
    font-size: 40px; font-weight: 400; color: var(--ink); line-height: 1;
  }
  .brand-dot { width: 14px; height: 14px; border-radius: 50%; background: var(--blue); }
  .brand-tagline {
    margin-top: 8px; font-size: 13px; font-style: italic; color: var(--grey);
  }

  .contact-list { position: absolute; left: 34px; top: 132px; list-style: none; }
  .contact-item {
    display: flex; align-items: center; gap: 8px;
    font-size: 11.5px; color: var(--grey); line-height: 20px;
  }
  .contact-icon {
    width: 13px; height: 13px; border-radius: 50%;
    background: var(--blue); flex: none;
    display: flex; align-items: center; justify-content: center;
  }
  .contact-icon svg { width: 9px; height: 9px; }

  .holder { position: absolute; right: 30px; bottom: 24px; text-align: right; }
  .holder-name { font-size: 16px; font-weight: 600; color: var(--blue); }
  .holder-creds { font-size: 12px; color: var(--grey); margin-top: 2px; }

  .back-brand {
    position: absolute; left: 0; right: 0; top: 82px;
    display: flex; justify-content: center; align-items: center; gap: 10px;
    font-size: 40px; font-weight: 400; color: #ffffff; line-height: 1;
  }
  .back-brand .brand-dot { background: #ffffff; }
  .back-accent {
    position: absolute; right: -60px; bottom: -90px;
    width: 260px; height: 260px; border-radius: 50%;
    background: rgba(255,255,255,0.12);
  }
  .back-web {
    position: absolute; right: 30px; bottom: 28px;
    font-size: 14px; font-weight: 600; font-style: italic; color: #ffffff;
  }
</style>
</head>
<body>

  <section class="card card-front" aria-label="Business card front">
    <svg class="front-swoosh" viewBox="0 0 540 310" aria-hidden="true">
      <path d="M300 0 C390 30 480 110 540 235 L540 0 Z" fill="#6aa7e6"/>
      <path d="M318 0 C400 32 485 110 540 218 L540 0 Z" fill="#3f87d4"/>
      <path d="M420 40 C470 80 510 130 540 190 L540 55 C505 50 460 44 420 40 Z" fill="#111111"/>
      <path d="M440 70 C480 100 512 140 534 182" stroke="#3f87d4" stroke-width="6" fill="none"/>
      <path d="M470 62 C500 86 524 118 538 150" stroke="#6aa7e6" stroke-width="4" fill="none"/>
    </svg>

    <div class="brand">
      <div class="brand-name"><span>Bright Ferns</span><span class="brand-dot"></span></div>
      <p class="brand-tagline">Natural Wellness &amp; Live Cell Review</p>
    </div>

    <ul class="contact-list">
      <li class="contact-item"><span class="contact-icon"><svg viewBox="0 0 10 10"><rect x="2" y="2" width="6" height="7" fill="#fff"/></svg></span>Larkvale Acupuncture Clinic</li>
      <li class="contact-item"><span class="contact-icon"><svg viewBox="0 0 10 10"><path d="M5 9 L2 5 A3 3 0 1 1 8 5 Z" fill="#fff"/></svg></span>2736-18 Avenue, Suite 200</li>
      <li class="contact-item"><span class="contact-icon"><svg viewBox="0 0 10 10"><path d="M5 9 L2 5 A3 3 0 1 1 8 5 Z" fill="#fff"/></svg></span>Larkvale, AB T8K 2P6</li>
      <li class="contact-item"><span class="contact-icon"><svg viewBox="0 0 10 10"><path d="M2 1 L4 1 L5 3 L4 4 Q5 6 6 6 L7 5 L9 6 L9 8 Q5 9 2 5 Q1 3 2 1 Z" fill="#fff"/></svg></span>780.555.0148</li>
      <li class="contact-item"><span class="contact-icon"><svg viewBox="0 0 10 10"><rect x="1.5" y="2.5" width="7" height="5" fill="#fff"/><path d="M1.5 2.5 L5 5.5 L8.5 2.5" stroke="#3f87d4" fill="none"/></svg></span>brightferns@mailnest.ca</li>
      <li class="contact-item"><span class="contact-icon"><svg viewBox="0 0 10 10"><circle cx="5" cy="5" r="3.5" fill="none" stroke="#fff"/><line x1="1.5" y1="5" x2="8.5" y2="5" stroke="#fff"/></svg></span>www.brightfernsnaturalwellness.com</li>
    </ul>

    <div class="holder">
      <p class="holder-name">Marla Dunwoody</p>
      <p class="holder-creds">DynBC, CH, BA</p>
    </div>
  </section>

  <section class="card card-back" aria-label="Business card back">
    <div class="back-accent"></div>
    <div class="back-brand"><span>Bright Ferns</span><span class="brand-dot"></span></div>
    <p class="back-web">www.BrightFernsNaturalWellness.com</p>
  </section>

</body>
</html>
```